Stationary Designs for Quorvanet.com
#117 I like your design. Please add info@quorvanet.example for the email address on the letterhead, fax, and envelopes.
Hello designers, thank you so much once again for your great designs. Please insert Tessel Rise TNQW under Marlow Parish. Also,I have rated the business cards. Are you able to show envelopes, fax form, letterhead etc for the stationary?
I shall be selecting a winner by tomorrow.
can you upload vector logo?

```html
<!DOCTYPE html>
<html lang="en">
<head>
<meta charset="utf-8">
<title>Quorvanet.com Stationery</title>
<link href="https://fonts.googleapis.com/css2?family=Nunito:wght@700&family=Open+Sans:wght@400;600;700&display=swap" rel="stylesheet">
<style>
  :root{
    --bg:#3a3a3a;
    --paper:#ffffff;
    --teal:#1f9aa3;
    --teal-light:#7fd0d4;
    --sky:#3aa8e0;
    --navy:#14243a;
    --ink:#2d3a45;
    --muted:#7b8790;
    --rule:#b9c3ca;
    --map:#e3eef0;
  }
  *{box-sizing:border-box;margin:0;padding:0}
  html,body{width:1200px;height:557px;overflow:hidden}
  body{background:var(--bg);font-family:"Open Sans",Arial,sans-serif;color:var(--ink);position:relative}
  .piece{position:absolute;background:var(--paper);overflow:hidden;box-shadow:0 4px 14px rgba(0,0,0,.35)}
  .wave{position:absolute;left:0;bottom:0;width:100%;display:block}
  .logo{display:flex;align-items:center;gap:5px;font-family:"Nunito",Arial,sans-serif;font-weight:700;color:var(--teal);white-space:nowrap}
  .logo-dot{width:.7em;height:.7em;border-radius:50%;background:var(--teal)}
  .small{font-size:6px;line-height:1.45;color:var(--muted)}

  /* business card front */
  .card-front{left:30px;top:70px;width:200px;height:114px}
  .card-front .logo{position:absolute;left:12px;top:12px;font-size:15px}
  .card-holder{position:absolute;right:12px;top:44px;text-align:right}
  .card-holder .name{font-size:10px;font-weight:700;color:var(--navy)}
  .card-holder .role{font-size:6.5px;color:var(--muted)}
  .card-holder .small{margin-top:3px}

  /* business card back */
  .card-back{left:245px;top:70px;width:200px;height:114px}
  .card-back .logo{position:absolute;left:50%;top:28px;transform:translateX(-50%);font-size:16px}
  .card-back .url{position:absolute;right:12px;bottom:40px;font-size:6.5px;color:var(--muted)}

  /* envelope */
  .envelope{left:30px;top:215px;width:415px;height:208px}
  .envelope .logo{position:absolute;left:18px;top:16px;font-size:19px}
  .envelope .return{position:absolute;left:18px;top:44px}

  /* sheets */
  .sheet{top:40px;width:330px;height:477px}
  .fax{left:500px}
  .letterhead{left:850px}
  .sheet .logo{position:absolute;left:22px;top:26px;font-size:20px}
  .sheet .address{position:absolute;left:190px;top:20px}
  .fax-title{position:absolute;right:22px;top:96px;font-size:14px;font-weight:700;color:var(--navy);letter-spacing:.5px}
  .fax-table{position:absolute;left:22px;top:116px;width:286px;border:1px solid var(--rule);border-collapse:collapse;font-size:6px;font-weight:600;color:var(--navy)}
  .fax-table td{height:17px;padding:0 5px;border-bottom:1px solid var(--rule);width:25%}
  .fax-table td.line{border-bottom:1px solid var(--rule)}
  .comments{position:absolute;left:22px;top:194px;font-size:6.5px;font-weight:700;color:var(--navy)}
  .map-area{position:absolute;left:60px;top:230px;width:210px;height:110px;background:radial-gradient(ellipse at center,var(--map) 0%,rgba(227,238,240,0) 70%)}
</style>
</head>
<body>

<!-- Business card front -->
<section class="piece card-front">
  <div class="logo"><span class="logo-dot"></span>Quorvanet.com</div>
  <div class="card-holder">
    <p class="name">Dana Ellery</p>
    <p class="role">Sales Manager</p>
    <p class="small">Tel 441 555 0142<br>info@quorvanet.example</p>
  </div>
  <svg class="wave" viewBox="0 0 200 36" height="36" preserveAspectRatio="none" aria-hidden="true">
    <path d="M0,16 C60,0 120,34 200,8 L200,36 L0,36Z" fill="var(--teal-light)"/>
    <path d="M0,22 C70,6 130,36 200,14 L200,36 L0,36Z" fill="var(--teal)"/>
    <path d="M0,20 C70,4 130,34 200,12" fill="none" stroke="var(--navy)" stroke-width="2"/>
  </svg>
</section>

<!-- Business card back -->
<section class="piece card-back">
  <div class="logo"><span class="logo-dot"></span>Quorvanet.com</div>
  <p class="url">www.quorvanet.example</p>
  <svg class="wave" viewBox="0 0 200 36" height="36" preserveAspectRatio="none" aria-hidden="true">
    <path d="M0,12 C60,30 130,0 200,18 L200,36 L0,36Z" fill="var(--sky)"/>
    <path d="M0,20 C70,34 130,6 200,24 L200,36 L0,36Z" fill="var(--teal)"/>
    <path d="M0,18 C70,32 130,4 200,22" fill="none" stroke="var(--navy)" stroke-width="2"/>
  </svg>
</section>

<!-- Envelope -->
<section class="piece envelope">
  <div class="logo"><span class="logo-dot"></span>Quorvanet.com</div>
  <p class="small return">P.O. Box 2214<br>Marlow Parish<br>Tessel Rise TNQW<br>info@quorvanet.example</p>
  <svg class="wave" viewBox="0 0 415 50" height="50" preserveAspectRatio="none" aria-hidden="true">
    <path d="M160,50 C240,40 320,10 415,6 L415,50Z" fill="var(--teal-light)"/>
    <path d="M200,50 C270,42 340,20 415,16 L415,50Z" fill="var(--teal)"/>
    <path d="M190,50 C260,40 335,16 415,12" fill="none" stroke="var(--navy)" stroke-width="2"/>
  </svg>
</section>

<!-- Fax sheet -->
<section class="piece sheet fax">
  <div class="logo"><span class="logo-dot"></span>Quorvanet.com</div>
  <p class="small address">P.O. Box 2214<br>Marlow Parish<br>Tessel Rise TNQW<br>Tel 441 555 0142<br>Fax 441 555 0143<br>info@quorvanet.example<br>www.quorvanet.example</p>
  <h1 class="fax-title">FAX</h1>
  <table class="fax-table">
    <tr><td>TO:</td><td class="line"></td><td>FROM:</td><td class="line"></td></tr>
    <tr><td>FAX:</td><td class="line"></td><td>PAGES:</td><td class="line"></td></tr>
    <tr><td>PHONE:</td><td class="line"></td><td>DATE:</td><td class="line"></td></tr>
    <tr><td>RE:</td><td class="line"></td><td>CC:</td><td class="line"></td></tr>
  </table>
  <p class="comments">COMMENTS:</p>
  <div class="map-area" role="img" aria-label="Faint island map watermark"></div>
  <svg class="wave" viewBox="0 0 330 70" height="70" preserveAspectRatio="none" aria-hidden="true">
    <path d="M0,30 C100,0 200,60 330,20 L330,70 L0,70Z" fill="var(--teal-light)"/>
    <path d="M0,40 C110,12 210,70 330,30 L330,70 L0,70Z" fill="var(--teal)"/>
    <path d="M0,36 C110,8 210,66 330,26" fill="none" stroke="var(--navy)" stroke-width="2.5"/>
  </svg>
</section>

<!-- Letterhead -->
<section class="piece sheet letterhead">
  <div class="logo"><span class="logo-dot"></span>Quorvanet.com</div>
  <p class="small address">P.O. Box 2214<br>Marlow Parish<br>Tessel Rise TNQW<br>Tel 441 555 0142<br>Fax 441 555 0143<br>info@quorvanet.example<br>www.quorvanet.example</p>
  <div class="map-area" role="img" aria-label="Faint island map watermark"></div>
  <svg class="wave" viewBox="0 0 330 70" height="70" preserveAspectRatio="none" aria-hidden="true">
    <path d="M0,30 C100,0 200,60 330,20 L330,70 L0,70Z" fill="var(--teal-light)"/>
    <path d="M0,40 C110,12 210,70 330,30 L330,70 L0,70Z" fill="var(--teal)"/>
    <path d="M0,36 C110,8 210,66 330,26" fill="none" stroke="var(--navy)" stroke-width="2.5"/>
  </svg>
</section>

</body>
</html>
```